Velqora new official website

We need a new design for our website www.velqora-example.com We are web marketing publishers and our website must be attractive for clients. That's why we need to "refresh" it. The main colour of our logo is orange, and this is an indication for the colours of the website too. We need the design for the homepage and the design of inner pages. Here is the list of the various sections of the website:
- ABOUT US: Who we are/Certificates/Offices/Team
- SERVICES: SEM/Display/Email Marketing and coregistration/ad networking
- PROJECTS/NETWORK/BRANDS: We need one page per country with screenshots of the websites and very short descriptions.
- VELQORA & CHARITY
- WORK WITH US
- CONTACT US
- NEWS

```html
<!DOCTYPE html>
<html lang="en">
<head>
<meta charset="utf-8">
<title>Velqora – Home</title>
<link href="https://fonts.googleapis.com/css2?family=Arimo:wght@400;700&display=swap" rel="stylesheet">
<style>
:root{
  --orange:#f07c0a;
  --orange-light:#f7a23a;
  --orange-dark:#e06a00;
  --ink:#222;
  --grey-text:#444;
  --nav-top:#ececec;
  --nav-bottom:#c9c9c9;
  --pill:#6e6e6e;
  --card-bg:#f2f2f2;
  --border:#c8c8c8;
  --news-bg:#e1e1e1;
  --footer:#353535;
  --white:#fff;
}
*{box-sizing:border-box;margin:0;padding:0}
html,body{width:1024px;height:1200px;overflow:hidden}
body{position:relative;background:var(--white);font-family:"Arimo",Arial,sans-serif;color:var(--ink)}
.abs{position:absolute}

/* header */
.brand{left:50px;top:28px;display:flex;align-items:center;gap:8px}
.brand-name{font-size:38px;font-weight:700;color:var(--orange);letter-spacing:-1px}
.brand-dot{width:30px;height:30px;border-radius:50%;background:var(--orange)}
.search{left:787px;top:52px;width:212px;height:31px;border:1px solid #cfcfcf;border-radius:3px;display:flex;align-items:center;font-size:13px;color:#333;padding-left:9px}
.search-btn{position:absolute;right:0;top:0;width:29px;height:29px;border-left:1px solid #cfcfcf;background:#f3f3f3;display:flex;align-items:center;justify-content:center}
.rule{left:0;top:99px;width:1024px;height:5px;background:var(--orange)}
.nav{left:0;top:104px;width:1024px;height:41px;background:linear-gradient(var(--nav-top),var(--nav-bottom));display:flex;align-items:center;padding-left:22px;font-size:13px;color:#222}
.nav a{color:inherit;text-decoration:none;padding:4px 13px;margin-right:6px}
.nav a.active{background:var(--pill);color:var(--white);border-radius:11px}

/* hero */
.hero{left:0;top:145px;width:1024px;height:270px;background:linear-gradient(90deg,var(--orange-light),var(--orange) 45%,var(--orange-dark))}
.hero-photo{left:400px;top:145px;width:624px;height:270px;background:linear-gradient(100deg,rgba(240,124,10,0) 0%,#f0c8a0 35%,#f3ece4 55%,#e9b48c 85%,#f0a060)}
.hero-title{left:30px;top:236px;width:380px;text-align:center;font-size:37px;line-height:44px;color:#3a3a3a;text-shadow:0 1px 0 rgba(255,255,255,.35)}
.hero-title b{font-weight:700}

/* expertise */
.section-title{left:22px;top:436px;font-size:20px;color:#222}
.fields{left:22px;top:464px;width:980px;height:212px;border:1px solid var(--border);border-radius:6px;overflow:hidden;display:flex;background:linear-gradient(#fafafa,#e8e8e8)}
.field{border-right:1px solid var(--border);position:relative}
.field:last-child{border-right:0}
.field-head{height:60px;background:linear-gradient(var(--orange-light),var(--orange-dark));color:var(--white);font-size:18px;line-height:18px;display:flex;align-items:center;padding:0 16px 0 20px}
.field-body{padding:10px 14px 0 20px;font-size:12px;line-height:14.4px;color:var(--grey-text)}
.more{display:block;text-align:right;color:#333;text-decoration:underline}

/* columns */
.col{top:708px;width:270px}
.col h2{font-size:16px;font-weight:400;color:var(--orange);padding:0 0 6px 2px;border-bottom:1px solid #555;margin-bottom:8px}
.col p{font-size:12px;line-height:14.3px;color:var(--ink)}
.col .link{display:block;text-align:right;color:var(--orange);font-size:12px;text-decoration:underline;margin-top:1px}

.news{left:692px;top:698px;width:310px;height:204px;background:var(--news-bg);border-radius:6px;padding:12px 20px 0 18px}
.news h2{font-size:16px;font-weight:400;color:#111;padding-bottom:6px;border-bottom:1px solid #555;margin-bottom:14px}
.news-item{font-size:12px;line-height:14px;margin-bottom:28px}
.news-item b{color:var(--orange);display:block}

/* footer */
.footer{left:0;top:955px;width:1024px;height:245px;background:var(--footer);color:var(--white)}
.foot-nav{left:10px;top:13px;font-size:10px;display:flex;gap:9px}
.copy{left:9px;top:28px;font-size:12px}
.offices{right:10px;top:14px;text-align:right;font-size:12px;line-height:14px}
.offices p{margin-bottom:15px}
</style>
</head>
<body>

<header>
  <div class="abs brand"><span class="brand-name">Velqora</span><span class="brand-dot"></span></div>
  <div class="abs search">Search
    <span class="search-btn"><svg width="18" height="18" viewBox="0 0 18 18"><circle cx="7" cy="7" r="5.5" fill="none" stroke="#666" stroke-width="2"/><line x1="11" y1="11" x2="16" y2="16" stroke="#666" stroke-width="3" stroke-linecap="round"/></svg></span>
  </div>
  <div class="abs rule"></div>
  <nav class="abs nav">
    <a class="active">HOME</a><a>ABOUT US</a><a>SERVICES</a><a>PROJECTS</a><a>VELQORA &amp; CHARITY</a><a>WORK WITH US</a><a>CONTACT US</a><a>NEWS</a>
  </nav>
</header>

<section>
  <div class="abs hero"></div>
  <div class="abs hero-photo" role="img" aria-label="Photo of hands sketching a light bulb idea on paper with an orange pen"></div>
  <h1 class="abs hero-title" style="font-weight:400">THE <b>MAIN</b> WAY TO<br>YOUR BUSINESS</h1>
</section>

<section>
  <h2 class="abs section-title" style="font-weight:400">Fields of Expertise</h2>
  <div class="abs fields">
    <div class="field" style="width:198px"><div class="field-head">Tourism</div><div class="field-body">Tourism has been our first passion.Today it is our MAIN business and generates our MAIN income.<a class="more">read more</a></div></div>
    <div class="field" style="width:195px"><div class="field-head">Technologies &amp; Communication</div><div class="field-body">Dsl, lap tops, hardware, isn't that a hard job to keep updated about it?<a class="more">read more</a></div></div>
    <div class="field" style="width:198px"><div class="field-head">Finance</div><div class="field-body">VELQORA has been working for a long time with the MAIN brands in the international world of finance.<a class="more">read more</a></div></div>
    <div class="field" style="width:191px"><div class="field-head">Fashion</div><div class="field-body">The new frontier for our company is the world of fashion; We believe that today, television and the Internet are merging, at least when it comes to advertising and reaching potential cus-tomers.<a class="more">read more</a></div></div>
    <div class="field" style="flex:1"><div class="field-head">Durable Goods</div><div class="field-body">As publisher we help the MAIN brands in the field of automotive, appliances, business equipment, elec-tronic equipment, electronic equipment, home furnishings and fixtures...<a class="more">read more</a></div></div>
  </div>
</section>

<section>
  <div class="abs col" style="left:44px">
    <h2>Scope and Mission</h2>
    <p>Our aim is creating adding value on our custom-ers sales through technology and web marketing by means of the most modern web advertising systems. We help our customers in developing new sales stretegies based on the web market-ing. We watch the market and support our cus-tomers in achieving excellent visibility on the newest advertising channels. We are able to offer a wide range of either standard or tailored solu-tions.</p>
    <a class="link">Read More</a>
  </div>
  <div class="abs col" style="left:365px">
    <h2>Clients' strategies and web know how</h2>
    <p>We cooperate with the MAIN international brands in the fields of tourism, finance, fashion, durable goods, technologies &amp; communication. We help our customers in finding the way to succeed on every single one of their campaigns and on the brand awareness. We implement our strategies also in cooperation with some well known inter-national partners who cooperate with us in tracing and checking statistics and perfor-mances.</p>
    <a class="link">Read More</a>
  </div>
  <aside class="abs news">
    <h2>Latest News</h2>
    <div class="news-item"><b>10% of Search Ad Clicks From Mobile</b>Mobile search ad clicks grew 230 percent in the past year, according to Clickmetrix.</div>
    <div class="news-item"><b>Greater U.S. Reach for Pomelo PomOS Than Vantor Droidal Across Devices</b>Though Droidal powers more smartphones, Pomelo's reach is boosted by Player and Tab.</div>
  </aside>
</section>

<footer class="abs footer">
  <div class="abs foot-nav"><span>HOME</span><span>ABOUT US</span><span>SERVICES</span><span>PROJECTS</span><span>VELQORA &amp; CHARITY</span><span>WORK WITH US</span><span>CONTACT US</span><span>NEWS</span></div>
  <div class="abs copy">Copyright © 2011. Velqora.</div>
  <div class="abs offices">
    <p>HEAD OFFICE: Velqora srl - Via delle Rose 14<br>65100 Pescara (PE) - ITALY<br>Tel.+39 0850000123 Fax +39 (0)2 700000456</p>
    <p>BRANCH OFFICE: B-9 Lotus Block, Techpark<br>695000 Thiruvananthapuram - INDIA</p>
    <p>BRANCH OFFICE: Meridian House, Sunrise Road<br>tel 01100000321 New Delhi - INDIA</p>
    <p>BRANCH OFFICE: Carrer del Sol 21, 2-1<br>08000 Barcelona - España</p>
  </div>
</footer>

</body>
</html>
```